Business card for Quorvane LLC | ||
Design a business card for a geospatial startup | ||
Use same font as used in my logo | ||
Cutting-Edge Corporate Modern Professional Simple |
Peter Hollis | ||
Chief Technical Officer | ||
48 Linden Row Suite 200 Bramwick, ST, 55821-3307 |
hello@quorvane-mail.net | ||
www.quorvane-site.net | ||
I''l provide the actual information once we get rolling :) I'd like to incorporate the corporate logo onto the card. Please keep the colors in the logo. You can use any font that looks good. |

```html
<!DOCTYPE html>
<html lang="en">
<head>
<meta charset="utf-8">
<title>Quorvane LLC — Business Card</title>
<link rel="stylesheet" href="https://fonts.googleapis.com/css2?family=PT+Sans:wght@400;700&family=Tinos:wght@400&display=swap">
<style>
  :root {
    --backdrop: #7a7a7a;
    --card-white: #ffffff;
    --brand-navy: #1f4f8f;
    --band-blue: #2f5da6;
    --accent-green: #8cc63f;
    --ink: #2a2a2a;
    --rule: #9a9a9a;
    --icon-blue: #3a6db5;
  }
  * { margin: 0; padding: 0; box-sizing: border-box; }
  html, body { width: 1200px; height: 780px; overflow: hidden; }
  body {
    background: var(--backdrop);
    display: flex;
    align-items: center;
    justify-content: center;
  }
  .business-card {
    position: relative;
    width: 1050px;
    height: 600px;
    background: var(--card-white);
    border-radius: 34px;
    overflow: hidden;
  }
  .card-bands {
    position: absolute;
    inset: 0;
    width: 100%;
    height: 100%;
  }
  .brand-name {
    position: absolute;
    top: 78px;
    left: 0;
    width: 100%;
    text-align: center;
    font-family: "PT Sans", sans-serif;
    font-weight: 700;
    font-size: 112px;
    letter-spacing: -2px;
    color: var(--brand-navy);
    line-height: 1;
  }
  .address-block {
    position: absolute;
    top: 248px;
    right: 565px;
    text-align: right;
    font-family: "Tinos", serif;
    font-size: 25px;
    line-height: 1.45;
    color: var(--ink);
  }
  .divider {
    position: absolute;
    top: 238px;
    left: 510px;
    width: 1px;
    height: 120px;
    background: var(--rule);
  }
  .contact-list {
    position: absolute;
    top: 238px;
    left: 530px;
    list-style: none;
    font-family: "Tinos", serif;
    font-size: 25px;
    color: var(--ink);
  }
  .contact-list li {
    display: flex;
    align-items: center;
    gap: 12px;
    height: 40px;
  }
  .contact-icon { width: 22px; height: 22px; flex: none; }
  .person {
    position: absolute;
    right: 48px;
    top: 438px;
    text-align: right;
    font-family: "PT Sans", sans-serif;
    color: var(--card-white);
  }
  .person-name { font-size: 38px; font-weight: 700; line-height: 1.1; }
  .person-title { font-size: 24px; font-weight: 400; margin-top: 4px; }
</style>
</head>
<body>
  <div class="business-card">
    <svg class="card-bands" viewBox="0 0 1050 600" aria-hidden="true">
      <path d="M0 420 C 320 560 700 525 1050 320 V600 H0 Z" fill="var(--accent-green)"/>
      <path d="M0 446 C 330 590 720 552 1050 350 V600 H0 Z" fill="var(--band-blue)"/>
    </svg>

    <div class="brand-name">Quorvane</div>

    <address class="address-block" style="font-style: normal;">
      48 Linden Row<br>
      Suite 200<br>
      Bramwick, ST, 55821-3307
    </address>

    <div class="divider"></div>

    <ul class="contact-list">
      <li>
        <svg class="contact-icon" viewBox="0 0 22 22" aria-hidden="true">
          <path d="M6 3 L9 7 L7.5 9 C8.5 11.5 10.5 13.5 13 14.5 L15 13 L19 16 L17 19 C10 19 3 12 3 5 Z" fill="var(--icon-blue)"/>
        </svg>
        <span>(555) 014-2290</span>
      </li>
      <li>
        <svg class="contact-icon" viewBox="0 0 22 22" aria-hidden="true">
          <circle cx="11" cy="11" r="10" fill="var(--icon-blue)"/>
          <circle cx="11" cy="11" r="3.2" fill="none" stroke="#fff" stroke-width="1.8"/>
          <path d="M14.2 8 V12.5 C14.2 14.5 17 14.5 17 12 A6 6 0 1 0 14 16.2" fill="none" stroke="#fff" stroke-width="1.6"/>
        </svg>
        <span>hello@quorvane-mail.net</span>
      </li>
      <li>
        <svg class="contact-icon" viewBox="0 0 22 22" aria-hidden="true">
          <circle cx="11" cy="11" r="10" fill="var(--icon-blue)"/>
          <ellipse cx="11" cy="11" rx="4" ry="8" fill="none" stroke="#fff" stroke-width="1.4"/>
          <line x1="3" y1="11" x2="19" y2="11" stroke="#fff" stroke-width="1.4"/>
        </svg>
        <span>www.quorvane-site.net</span>
      </li>
    </ul>

    <div class="person">
      <div class="person-name">Peter Hollis</div>
      <div class="person-title">Chief Technical Officer</div>
    </div>
  </div>
</body>
</html>
```